Retail healthy snack bar design

We are launching a new product range to be sold in health food stores.

The Fennick Co (no logo as yet).

We will have a range of bars, spreads (jars), shakes (bags) in the following ranges-
milk protein
plant protein
keto

For this project, please do a bar design. The chosen designer will be given additional work for the rest of the packaging as well as promotional material such as social media, banners, posters etc.

Lumo Bar Protein - Must be White to be recognized.
Lumo Bar Collagen - Bronze
Lumo Keto Bar - Possibly Red
Lumo Bar Plant - Green

Food images can be added but their must be samples without as we may need to remove for certain countries.

Target Market(s)

Healthy, Weight-loss, Bodybuilding, Elderly, Medical

Industry/Entity Type

Health And Wellness

Font styles to use
Sans Serif

Colors

Designer to choose colors to be used in the design.

Requirements
Must have
• Clean simple to read design with minimal colours

Flavour to be easily read (Must include the word 'Flavour' in the same size font as the flavour description)

Must show size of bar (60g).

Some details that can be added (optional)-
raw, cold pressed bar with (example) whey protein isolate + prebiotic fibre
natural, with no artificial colours, flavours, preservatives or sweeteners
no added sugar or sugar alcohols - gluten free - soy free

Rear of bar shall remain the same or all same details if redesigned.
Nice to have
• Clean design, use of silver foil and/or matt/gloss affect, large oversized flavour image (if including).

See images of current designs I like on the market for ideas
Should not have
• Too many images (if any).

```html
<!DOCTYPE html>
<html lang="en">
<head>
<meta charset="utf-8">
<title>Lumo Bar Range</title>
<link rel="stylesheet" href="https://fonts.googleapis.com/css2?family=Alfa+Slab+One&family=Comfortaa:wght@400;700&display=swap">
<style>
  :root {
    --page: #e9e9e9;
    --ink: #0d0d0d;
    --bronze: #9b6a14;
    --protein-white: #f3f3f3;
    --paleo-orange: #f28c00;
    --keto-red: #e6140f;
    --slab: "Alfa Slab One", Georgia, serif;
    --round: "Comfortaa", Arial, sans-serif;
  }
  * { box-sizing: border-box; margin: 0; padding: 0; }
  html, body { width: 1200px; height: 1200px; overflow: hidden; }
  body {
    position: relative;
    background: radial-gradient(circle at 50% 40%, #f7f7f7 0%, var(--page) 75%);
    font-family: var(--round);
    color: var(--ink);
  }
  .range {
    position: absolute; inset: 0; overflow: hidden;
    display: flex; flex-direction: column; justify-content: center; align-items: center;
    gap: 40px;
  }
  .bar {
    --wrap: var(--protein-white);
    --on-ink: var(--protein-white);
    position: relative; flex: none;
    width: 1000px; height: 250px;
    background: var(--wrap);
  }
  .bar--collagen { --wrap: var(--bronze); --on-ink: var(--bronze); }
  .bar--protein { --wrap: var(--protein-white); --on-ink: #ffffff; }
  .bar--paleo { --wrap: var(--paleo-orange); --on-ink: var(--paleo-orange); }
  .bar--keto { --wrap: var(--keto-red); --on-ink: var(--keto-red); }

  .bar::before, .bar::after {
    content: ""; position: absolute; top: 0; width: 10px; height: 100%;
    background-size: 10px 20px;
  }
  .bar::before { left: -10px; background-image: conic-gradient(from 45deg at left, var(--wrap) 90deg, transparent 0); }
  .bar::after { right: -10px; background-image: conic-gradient(from -135deg at right, var(--wrap) 90deg, transparent 0); }

  .crimp {
    position: absolute; top: 0; width: 46px; height: 100%;
    background: repeating-linear-gradient(90deg, rgba(0,0,0,.07) 0 3px, rgba(255,255,255,.12) 3px 7px);
  }
  .crimp--left { left: 0; }
  .crimp--right { right: 0; }

  .burst {
    position: absolute; left: 40px; top: 0; width: 420px; height: 250px;
    background: radial-gradient(ellipse 60% 55% at 35% 60%, rgba(255,255,255,.95) 0%, rgba(255,255,255,.55) 35%, rgba(255,255,255,0) 70%);
  }
  .bar--protein .burst {
    background: radial-gradient(ellipse 60% 55% at 35% 60%, rgba(150,150,150,.45) 0%, rgba(170,170,170,.2) 40%, rgba(200,200,200,0) 70%);
  }

  .brand {
    position: absolute; left: 118px; top: 22px;
    font-family: var(--slab); font-size: 40px; letter-spacing: 22px; line-height: 1;
  }
  .intro {
    position: absolute; left: 390px; top: 18px;
    font-size: 16px; font-weight: 700; line-height: 1.25;
  }
  .name {
    position: absolute; left: 118px; top: 58px;
    font-family: var(--slab); font-size: 104px; line-height: 1; letter-spacing: 2px;
    font-weight: 400; white-space: nowrap;
  }
  .name__sub {
    display: inline-block; vertical-align: top; margin-top: 8px; margin-left: 4px;
    font-size: 34px; background: var(--ink); color: var(--on-ink); padding: 2px 6px 0;
    letter-spacing: 0;
  }
  .claim {
    position: absolute; left: 118px; top: 150px; width: 700px; height: 24px;
    background: var(--ink); color: var(--on-ink);
    font-size: 15px; line-height: 24px; padding-left: 10px; white-space: nowrap; overflow: hidden;
  }
  .type {
    position: absolute; left: 140px; top: 164px;
    font-family: var(--slab); font-size: 80px; line-height: 1;
  }
  .stats { position: absolute; left: 380px; top: 182px; display: flex; gap: 10px; }
  .hex {
    width: 64px; height: 56px; background: var(--ink); color: var(--on-ink);
    clip-path: polygon(25% 0, 75% 0, 100% 50%, 75% 100%, 25% 100%, 0 50%);
    display: flex; flex-direction: column; align-items: center; justify-content: center;
    font-weight: 700; line-height: 1;
  }
  .hex b { font-size: 17px; }
  .hex small { font-size: 8px; margin-top: 2px; }
  .weight {
    position: absolute; right: 110px; top: 78px; width: 70px; height: 70px;
    background: var(--ink); color: var(--on-ink);
    clip-path: polygon(50% 0,60% 14%,75% 7%,78% 23%,94% 25%,87% 40%,100% 50%,87% 60%,94% 75%,78% 77%,75% 93%,60% 86%,50% 100%,40% 86%,25% 93%,22% 77%,6% 75%,13% 60%,0 50%,13% 40%,6% 25%,22% 23%,25% 7%,40% 14%);
    display: flex; align-items: center; justify-content: center;
    font-weight: 700; font-size: 19px;
  }
  .free-from {
    position: absolute; left: 610px; top: 190px; width: 330px;
    font-family: var(--slab); font-size: 13px; line-height: 1.5; letter-spacing: .3px;
    text-align: right;
  }
</style>
</head>
<body>
<main class="range">

  <article class="bar bar--collagen">
    <div class="crimp crimp--left"></div><div class="crimp crimp--right"></div>
    <div class="burst" role="img" aria-label="White radiating burst graphic"></div>
    <div class="brand">LUMO</div>
    <p class="intro">Raw, cold pressed bar with<br>whey protein isolate+prebiotic fibre</p>
    <h2 class="name">COOCKIE<span class="name__sub">DOUGH</span></h2>
    <p class="claim">Natural, with no artificial colours, flavours, preservatives, or sweeteners</p>
    <div class="type">BAR</div>
    <div class="stats">
      <div class="hex"><b>&lt;20g</b><small>PROTEINE</small></div>
      <div class="hex"><b>&lt;3g</b><small>SUGAR</small></div>
      <div class="hex"><b>&lt;3g</b><small>CARBS</small></div>
    </div>
    <div class="weight">60g</div>
    <p class="free-from">/NO SUGAR /NO ALCOHOLS /NO ADDED SUGAR<br>/GLUTEN FREE /SOY FREE</p>
  </article>

  <article class="bar bar--protein">
    <div class="crimp crimp--left"></div><div class="crimp crimp--right"></div>
    <div class="burst" role="img" aria-label="Grey radiating burst graphic"></div>
    <div class="brand">LUMO</div>
    <p class="intro">Raw, cold pressed bar with<br>whey protein isolate+prebiotic fibre</p>
    <h2 class="name">PROTEIN</h2>
    <p class="claim">Natural, with no artificial colours, flavours, preservatives, or sweeteners</p>
    <div class="type">BAR</div>
    <div class="stats">
      <div class="hex"><b>&lt;20g</b><small>PROTEINE</small></div>
      <div class="hex"><b>&lt;3g</b><small>SUGAR</small></div>
      <div class="hex"><b>&lt;3g</b><small>CARBS</small></div>
    </div>
    <div class="weight">60g</div>
    <p class="free-from">/NO SUGAR /NO ALCOHOLS /NO ADDED SUGAR<br>/GLUTEN FREE /SOY FREE</p>
  </article>

  <article class="bar bar--paleo">
    <div class="crimp crimp--left"></div><div class="crimp crimp--right"></div>
    <div class="burst" role="img" aria-label="White radiating burst graphic"></div>
    <div class="brand">LUMO</div>
    <p class="intro">Raw, cold pressed bar with<br>whey protein isolate+prebiotic fibre</p>
    <h2 class="name">PALEO</h2>
    <p class="claim">Natural, with no artificial colours, flavours, preservatives, or sweeteners</p>
    <div class="type">BAR</div>
    <div class="stats">
      <div class="hex"><b>&lt;20g</b><small>PROTEINE</small></div>
      <div class="hex"><b>&lt;3g</b><small>SUGAR</small></div>
      <div class="hex"><b>&lt;3g</b><small>CARBS</small></div>
    </div>
    <div class="weight">60g</div>
    <p class="free-from">/NO SUGAR /NO ALCOHOLS /NO ADDED SUGAR<br>/GLUTEN FREE /SOY FREE</p>
  </article>

  <article class="bar bar--keto">
    <div class="crimp crimp--left"></div><div class="crimp crimp--right"></div>
    <div class="burst" role="img" aria-label="White radiating burst graphic"></div>
    <div class="brand">LUMO</div>
    <p class="intro">Raw, cold pressed bar with<br>whey protein isolate+prebiotic fibre</p>
    <h2 class="name">KETONE</h2>
    <p class="claim">Natural, with no artificial colours, flavours, preservatives, or sweeteners</p>
    <div class="type">BAR</div>
    <div class="stats">
      <div class="hex"><b>&lt;20g</b><small>PROTEINE</small></div>
      <div class="hex"><b>&lt;3g</b><small>SUGAR</small></div>
      <div class="hex"><b>&lt;3g</b><small>CARBS</small></div>
    </div>
    <div class="weight">60g</div>
    <p class="free-from">/NO SUGAR /NO ALCOHOLS /NO ADDED SUGAR<br>/GLUTEN FREE /SOY FREE</p>
  </article>

</main>
</body>
</html>
```